A Hair, Beauty and Nails Wholesalers Needs a Business Card Design

We need a business card design for our company which is being passed from parents to daughter, so we wont to re-launch the company with an updated, modern, sophisticated, elegant, chic and fresh look which still incorporates the original colour scheme of Hot Pink, Dark Grey and White. The original logo which is attached can be used on the card but we would like to see some designs with the logo and some without, as we have not yet decided if we want the logo on the card. The name of our company is 'Velmora Supplies' and the name of our website is VelmoraGlowandPolish.example.au. We specialise in supplying a massive range of Hair, Beauty and Nail products to the industry. We are based in QLD, Australia but ship many orders via our website all across Australia.

```html
<!DOCTYPE html>
<html lang="en">
<head>
<meta charset="utf-8">
<title>Velmora Supplies – Business Card</title>
<link href="https://fonts.googleapis.com/css2?family=Pinyon+Script&display=swap" rel="stylesheet">
<style>
  :root {
    --hot-pink: #d8246a;
    --pink-light: #e2478a;
    --pink-deep: #b81a3c;
    --dark-grey: #2b2b2d;
    --white: #ffffff;
    --ink: #1d1d1d;
    --stage: #1b1b1b;
  }
  html, body {
    margin: 0;
    width: 1200px;
    height: 1000px;
    overflow: hidden;
    background: var(--stage);
  }
  .canvas {
    position: relative;
    width: 1200px;
    height: 1000px;
  }
  .card {
    position: absolute;
    width: 560px;
    height: 320px;
    background: var(--white);
    overflow: hidden;
    font-family: "Pinyon Script", cursive;
    box-shadow: 0 10px 30px rgba(0,0,0,.5);
  }
  .card-bg {
    position: absolute;
    inset: 0;
    width: 100%;
    height: 100%;
  }
  .card-front { left: 80px; top: 560px; }
  .card-back  { left: 560px; top: 130px; }

  /* Front */
  .company {
    position: absolute;
    left: 16px;
    top: 24px;
    width: 200px;
    text-align: center;
    color: var(--ink);
    font-size: 30px;
    line-height: 1.1;
    margin: 0;
    font-weight: 400;
    white-space: nowrap;
  }
  .contact {
    position: absolute;
    right: 34px;
    top: 36px;
    text-align: right;
    color: var(--white);
    white-space: nowrap;
  }
  .contact .role { font-size: 26px; line-height: 1.15; }
  .contact .person { font-size: 26px; line-height: 1.15; }
  .contact .phone { font-size: 32px; line-height: 1.25; }
  .address {
    position: absolute;
    right: 28px;
    bottom: 22px;
    color: var(--white);
    font-size: 19px;
    white-space: nowrap;
  }

  /* Back */
  .brand-name {
    position: absolute;
    left: 150px;
    top: 40px;
    display: flex;
    align-items: center;
    gap: 12px;
    color: var(--hot-pink);
    font-size: 42px;
    white-space: nowrap;
  }
  .brand-dot {
    width: 16px;
    height: 16px;
    border-radius: 50%;
    background: var(--hot-pink);
  }
  .tagline {
    position: absolute;
    right: 34px;
    top: 150px;
    text-align: right;
    color: var(--ink);
    font-size: 22px;
    line-height: 1.15;
    margin: 0;
    white-space: nowrap;
  }
  .website {
    position: absolute;
    right: 30px;
    bottom: 40px;
    color: var(--hot-pink);
    font-size: 24px;
    white-space: nowrap;
  }
</style>
</head>
<body>
<main class="canvas">

  <section class="card card-front" aria-label="Business card front">
    <svg class="card-bg" viewBox="0 0 560 320" preserveAspectRatio="none" aria-hidden="true">
      <defs>
        <linearGradient id="pinkFade" x1="0" y1="1" x2="1" y2="0">
          <stop offset="0" stop-color="#b81a3c"/>
          <stop offset="0.55" stop-color="#d8246a"/>
          <stop offset="1" stop-color="#e2478a"/>
        </linearGradient>
      </defs>
      <polygon points="0,320 380,0 560,0 560,320" fill="url(#pinkFade)"/>
    </svg>
    <h1 class="company">Velmora<br>Supplies<br>Beauty and Nails</h1>
    <div class="contact">
      <div class="role">Manager</div>
      <div class="person">Marisa Thornbury</div>
      <div class="phone">(07) 5550 0123</div>
    </div>
    <div class="address">27 Larkspur Lane, Brindlewood, QLD, 4000 Australia</div>
  </section>

  <section class="card card-back" aria-label="Business card back">
    <svg class="card-bg" viewBox="0 0 560 320" preserveAspectRatio="none" aria-hidden="true">
      <polygon points="0,0 560,0 560,70 0,230" fill="#2b2b2d"/>
    </svg>
    <div class="brand-name"><span class="brand-dot"></span>Velmora Supplies</div>
    <p class="tagline">Supplying<br>a massive range of Hair,<br>Beauty and Nail products</p>
    <div class="website">http://www.velmoraglowandpolish.example.au/</div>
  </section>

</main>
</body>
</html>
```